Learn-to-Swim Program for Children's Day Camp (Walter Brisbane Fieldgrounds)

We are a children's camp with a robust swim instruction program and we need a series of 5 kid-friendly banners which list the skills learned in our swim program that can be hung up around each outdoor pool complex. All together there are 6 overarching levels and 12 sublevels (see attached). Except for the Level V & VI, each banner should be one overarching level and the 2-3 sublevels that define it.

Each swim level has a name, most of which are sea creatures, and we want to have a corresponding image/avatar to go with the swim level name (e.g. tadpole, barracuda, orca, goldfish, catfish).

The banners should be 3 feet (width) by 5 feet (height). The banners will be hung outdoors so it needs a color scheme that won't get lost in the sunlight.

We will want to include our logo but do not need the design to match our logo colors. Logo can be in black or white.

Our website is: www.campwbf.org

Target Market(s)

children age 5 - 12

Industry/Entity Type

children's day camp

Requirements
Must have
• A progression from level I to level VI. Should have a happy, bright, fun, tone, text MUST be legible from at least a 5 foot distance
Should not have
• adult themes, a scheme that evokes sadness or fear

```html
<!DOCTYPE html>
<html lang="en">
<head>
<meta charset="utf-8">
<title>ARC III – Swim Levels</title>
<link href="https://fonts.googleapis.com/css2?family=Fredoka:wght@600;700&family=Asap+Condensed:wght@500;600&display=swap" rel="stylesheet">
<style>
  :root {
    --sun: #f9d86a;
    --sun-light: #f4de8e;
    --gold-edge: #c9a238;
    --sky-top: #c6e6f2;
    --sky-mid: #76c8ea;
    --sky-deep: #4f72bf;
    --ink-blue: #1a6fc0;
    --frame-blue: #1b6fc2;
    --white: #ffffff;
  }
  * { box-sizing: border-box; margin: 0; padding: 0; }
  html, body { width: 720px; height: 1200px; overflow: hidden; }
  body {
    position: relative;
    background: linear-gradient(to bottom, var(--sky-top) 11%, var(--sky-mid) 55%, #6aaede 78%, var(--sky-deep) 100%);
    font-family: "Asap Condensed", sans-serif;
  }
  .header {
    position: absolute; left: 0; top: 0; width: 720px; height: 131px;
    background: var(--sun);
    border-bottom: 10px solid var(--sun-light);
  }
  .title {
    position: absolute; left: 0; right: 0; top: 8px;
    text-align: center;
    font-family: "Fredoka", sans-serif; font-weight: 700;
    font-size: 96px; line-height: 1; letter-spacing: -2px;
    color: var(--white);
    -webkit-text-stroke: 9px var(--gold-edge);
    paint-order: stroke fill;
  }
  .outlined {
    position: absolute;
    font-family: "Fredoka", sans-serif; font-weight: 700;
    color: var(--white);
    -webkit-text-stroke: 6px var(--frame-blue);
    paint-order: stroke fill;
    line-height: 1;
  }
  .level-tag { font-size: 34px; }
  .level-name { font-size: 58px; letter-spacing: 1px; }
  .skills-tag { font-size: 36px; }
  .moveup-tag { font-size: 36px; }
  .art { position: absolute; border-radius: 45% 50% 40% 50%; }
  .art-minnow { left: 70px; top: 240px; width: 235px; height: 175px; background: radial-gradient(circle at 60% 55%, #e2e79a, #a9cc46 70%, #b6d9e6 100%); }
  .art-goldfish { left: 75px; top: 590px; width: 245px; height: 165px; background: radial-gradient(circle at 45% 55%, #fbd68a, #f49a4a 65%, #e5764d 100%); }
  .art-catfish { left: 105px; top: 910px; width: 240px; height: 185px; background: radial-gradient(circle at 55% 55%, #4c5468, #343a4c 70%, #2a5f9e 100%); }
  .skills-box {
    position: absolute; left: 358px; width: 334px;
    border: 5px solid var(--frame-blue); border-bottom: none;
    border-radius: 0 28px 0 0;
  }
  .skills-box.light { border-color: var(--white); background: rgba(255,255,255,0.2); }
  .skills-list {
    list-style: none; padding: 13px 22px 0 24px;
    font-size: 16.5px; line-height: 19.4px; font-weight: 500;
  }
  .skills-list li { position: relative; padding-left: 22px; }
  .skills-list li::before {
    content: ""; position: absolute; left: 0; top: 8px;
    width: 4px; height: 4px; border-radius: 50%; background: currentColor;
  }
  .box-minnow { top: 163px; height: 263px; color: var(--ink-blue); }
  .box-goldfish { top: 522px; height: 240px; color: var(--white); }
  .box-catfish { top: 842px; height: 257px; color: var(--white); }
  .box-catfish .skills-list { padding-top: 10px; }
  .moveup {
    position: absolute; left: 205px; width: 488px;
    background: var(--white); border-radius: 30px;
    color: var(--ink-blue); font-size: 16.5px; line-height: 19.4px; font-weight: 500;
    padding: 12px 22px 0 28px;
  }
  .moveup-minnow { top: 423px; height: 63px; border: 5px solid var(--frame-blue); padding: 7px 16px 0 22px; }
  .moveup-goldfish { top: 760px; height: 56px; text-align: justify; text-align-last: left; padding-top: 9px; }
  .moveup-catfish { top: 1097px; height: 66px; padding-top: 11px; }
  .brand {
    position: absolute; left: 0; right: 0; top: 1176px; text-align: center;
    font-family: "Asap Condensed", sans-serif; font-weight: 600; font-size: 15px;
    color: var(--white); letter-spacing: 2px;
  }
</style>
</head>
<body>
  <header class="header"><h1 class="title">ARC III</h1></header>

  <section class="level-minnow">
    <div class="outlined level-tag" style="left:38px;top:145px;">Level</div>
    <div class="outlined level-name" style="left:38px;top:185px;">MINNOW</div>
    <div class="art art-minnow" role="img" aria-label="Cartoon green minnow swimming"></div>
    <div class="skills-box box-minnow">
      <ul class="skills-list">
        <li>Proper streamline body position (on back and stomach) with flutter kick</li>
        <li>Kick on stomach, arms to side, roll to back float, big breath in, back to kick on stomach</li>
        <li>Correct front crawl arm motion with side breathing</li>
        <li>Correct backstroke arm motion</li>
        <li>Demonstrate basic front crawl</li>
        <li>Demonstrate basic backstroke</li>
        <li>Can exit pool independently (elbows and knees)</li>
      </ul>
    </div>
    <div class="outlined skills-tag" style="left:356px;top:145px;">Skills</div>
    <div class="moveup moveup-minnow">Must perform basic front crawl and backstroke. Must jump into deep water, float and kick to the side of the pool independently</div>
    <div class="outlined moveup-tag" style="left:60px;top:437px;">Move-Up</div>
  </section>

  <section class="level-goldfish">
    <div class="outlined level-tag" style="left:38px;top:502px;">Level</div>
    <div class="outlined level-name" style="left:36px;top:543px;">GOLDFISH</div>
    <div class="art art-goldfish" role="img" aria-label="Cartoon orange goldfish"></div>
    <div class="skills-box light box-goldfish">
      <ul class="skills-list">
        <li>One arm up one arm down on stomach then to back</li>
        <li>Streamline on front roll to streamline on back</li>
        <li>Basic rhythmic breathing</li>
        <li>Demonstrates proper front crawl</li>
        <li>Demonstrates proper backstroke</li>
        <li>Treading 1 minute</li>
        <li>Basic elementary backstroke</li>
        <li>Side flutter kick</li>
        <li>Streamline roll to side kick</li>
      </ul>
    </div>
    <div class="outlined skills-tag" style="left:356px;top:503px;">Skills</div>
    <div class="moveup moveup-goldfish">Must complete deep water orientation, front crawl, and backstroke with stamina</div>
    <div class="outlined moveup-tag" style="left:60px;top:770px;">Move-Up</div>
  </section>

  <section class="level-catfish">
    <div class="outlined level-tag" style="left:38px;top:828px;">Level</div>
    <div class="outlined level-name" style="left:36px;top:868px;">CATFISH</div>
    <div class="art art-catfish" role="img" aria-label="Cartoon dark grey catfish"></div>
    <div class="skills-box light box-catfish">
      <ul class="skills-list">
        <li>Tread water for 2 min continuously</li>
        <li>Front crawl with rhythmic breathing, fingertip entry, arm reach and body roll consistent and with stamina</li>
        <li>Catch-up stroke with alternate breathing every 3 counts</li>
        <li>Front crawl with alternate breathing and side flutter kick</li>
        <li>Double arm backstroke with pull</li>
        <li>Backstroke switch</li>
        <li>Sitting and kneeling dives with streamline position</li>
      </ul>
    </div>
    <div class="outlined skills-tag" style="left:356px;top:826px;">Skills</div>
    <div class="moveup moveup-catfish">Must perform advanced front crawl with fingertip entry and rhythmic breathing consistently and with stamina</div>
    <div class="outlined moveup-tag" style="left:62px;top:1112px;">Move-Up</div>
  </section>

  <div class="brand">WBF</div>
</body>
</html>
```